South Florida Real Estate Brokerage Business

The name is HOME CALVINA REAL ESTATE.
The company is a Real estate realty based in Miami.
Is targeted to Latin American clients.
Must express luxury, and efficiency.
Target clients for properties around 250k to a million +.
Calvina means Royal in Latin.
Should communicate safety and knowledge of the product and transaction with a tech edge.

The web design needs to be a Social tool, with Friendlane and other media integration of some sort. Needs to have a Show case place, a Search place (MLS listings) with maps and filters.
Needs to reflect luxury but also mixed with a social edge capable of engaging clients or transition them to communicate with the page.
Include the logo from the uploaded files, feel free to change the color or font per webdesign.
This is a Front en design, layout and graphics.
Possible future programming if approved.
I can receive Quotes for the Code part.

Target Market(s)

Spanish and English speakers living in Latin America and Canada looking for apartments and houses to buy.

Industry/Entity Type

Business

Requirements
Must have
• Search area.
Neighbourhood area.
Could be a blog or news area.
Client registration.
Social Plugin
Nice to have
• Social linking to networks.
Log in with friendlane account.
Friendlane Like.

```html
<!DOCTYPE html>
<html lang="en">
<head>
<meta charset="utf-8">
<title>Home Calvina Real Estate</title>
<link href="https://fonts.googleapis.com/css2?family=Arimo:wght@400;700&display=swap" rel="stylesheet">
<style>
:root{
  --gold:#b89d5c;
  --gold-light:#d4bf8a;
  --gold-dark:#9c8148;
  --ink:#1d1a17;
  --ink-soft:#2b2622;
  --brown:#5a4520;
  --paper:#f4f4f4;
  --line:#d8d8d8;
  --red:#a8150c;
  --text:#333;
}
*{box-sizing:border-box;margin:0;padding:0}
html,body{width:1003px;height:1200px;overflow:hidden;background:#fff}
body{font-family:"Arimo",Arial,sans-serif;color:var(--text);position:relative}
.abs{position:absolute}

/* header */
.header{left:0;top:0;width:1003px;height:125px;background:linear-gradient(100deg,#fff 0,#fff 37%,#ececec 42%,#e6e6e6 100%)}
.header-rule{left:20px;top:103px;width:963px;height:1px;background:var(--gold)}
.brand{left:45px;top:14px;display:flex;flex-direction:column;align-items:center}
.brand-mark{width:58px;height:58px;background:var(--gold)}
.brand-name{margin-top:10px;font-size:22px;letter-spacing:1px;color:var(--ink);font-weight:400;line-height:1}
.brand-sub{margin-top:4px;font-size:12px;letter-spacing:1.5px;color:var(--ink);font-weight:400;line-height:1}
.login{left:625px;top:19px;width:160px;height:32px;border:1px solid #cfcfcf;border-radius:4px;background:linear-gradient(#fff,#ececec);display:flex;align-items:center;gap:10px;padding-left:4px;font-size:11px;color:#222}
.login i{width:26px;height:26px;border-radius:50%;background:#2a4f8a;display:block}
.social{display:flex;gap:10px;align-items:center}
.social span{display:flex;align-items:center;gap:3px;font-size:9px;color:#444}
.social b{width:10px;height:10px;display:block;border-radius:2px}
.social-top{left:820px;top:30px;flex-wrap:wrap;width:170px;row-gap:6px}

/* nav */
.nav{left:20px;top:125px;width:963px;height:42px;background:linear-gradient(#c8b27a,#b0955a);display:flex;align-items:center;font-size:13px;color:#fff}
.nav a{color:#fff;text-decoration:none}
.nav .home{background:var(--ink);height:42px;width:77px;display:flex;align-items:center;justify-content:center}
.nav .items{display:flex;gap:16px;padding-left:18px}
.nav .sep{color:#f4ecd8}
.search-box{left:757px;top:132px;width:213px;height:29px;border-radius:5px;background:#fff;border:1px solid #ddd;display:flex;align-items:center;gap:14px;padding-left:10px;font-size:10px;color:#aaa}

/* hero */
.hero{left:0;top:167px;width:1003px;height:338px;background:linear-gradient(90deg,#1c1815,#2a2420 50%,#1c1815)}
.hero-frame{left:29px;top:11px;width:945px;height:312px;background:#fff}
.hero-photo{left:8px;top:8px;width:929px;height:296px;background:linear-gradient(180deg,#6f9ed2 0%,#e8e4da 30%,#f0ece2 65%,#8aa06a 85%,#3c8fb4 100%)}
.hero-arrow{top:152px;width:30px;height:40px;background:#3a3a3a;display:flex;align-items:center;justify-content:center}
.hero-arrow.left{left:37px;border-radius:0 20px 20px 0}
.hero-arrow.right{left:938px;border-radius:20px 0 0 20px}

/* search bar */
.search-band{left:0;top:505px;width:1003px;height:115px;background:linear-gradient(#fff,#e6e6e6)}
.search-panel{left:30px;top:12px;width:946px;height:95px;border-radius:5px;background:linear-gradient(#cdb884,#b59a5f)}
.search-tag{left:0;top:0;width:170px;height:95px}
.search-tag span{position:absolute;left:42px;top:40px;color:#fff;font-size:14px}
.field{font-size:13px;color:#fff;display:flex;align-items:center;gap:8px}
.select{width:110px;height:20px;background:#fff;border:1px solid #bdbdbd;position:relative}
.select.sm{width:84px}
.select::after{content:"";position:absolute;right:2px;top:2px;width:14px;height:14px;background:linear-gradient(#d8e4f3,#a9bcd7);border-radius:2px}
.radio{width:11px;height:11px;border-radius:50%;background:#fff;border:1px solid #888;display:inline-block}
.radio.on{box-shadow:inset 0 0 0 2px #fff;background:#4a9a3a}
.btn-dark{background:linear-gradient(#2b2622,#0f0d0b);color:#fff;border-radius:5px;display:flex;align-items:center;justify-content:center;font-size:13px;box-shadow:0 2px 3px rgba(0,0,0,.35)}
.adv{font-size:11px;color:#fff}

/* feature row */
.register{left:25px;top:630px;width:217px;height:162px;border-radius:6px;background:linear-gradient(#f0f0f0,#dcdcdc);border:1px solid #d0d0d0}
.register h3{position:absolute;left:47px;top:8px;font-size:14px;font-weight:400;color:var(--brown)}
.register .in{position:absolute;left:19px;width:190px;height:24px;background:#fff;border:1px solid #c8c8c8;font-size:10px;color:#555;padding:6px 13px}
.card{top:630px;width:230px;height:162px;border:1px solid #ddd;background:#fff;padding:3px}
.card .photo{width:100%;height:131px}
.card .cap{height:26px;background:var(--ink-soft);color:#fff;font-size:13px;display:flex;align-items:center;justify-content:center}

/* lower */
.lower{left:0;top:808px;width:1003px;height:254px;background:var(--paper);border-top:1px solid #e6e6e6}
.lower h4{position:absolute;font-size:14px;font-weight:400;color:var(--brown);letter-spacing:.5px}
.post{position:absolute;font-size:10.5px;line-height:14px;color:#333;width:160px}
.post .date{display:block;margin-bottom:6px}
.avatar{position:absolute;width:58px;height:58px;border:1px solid #ddd;background:#fff;padding:3px}
.avatar div{width:100%;height:100%;background:linear-gradient(#9a8b70,#5d5448)}
.more{position:absolute;font-size:10.5px;color:var(--red)}
.listing{position:absolute;width:160px}
.listing .pic{width:140px;height:89px;border:1px solid #aaa}
.listing p{font-size:10.5px;line-height:14px;margin-top:10px}
.price{position:absolute;font-size:12.5px;color:var(--red)}
.dot{position:absolute;width:18px;height:18px;border-radius:50%;background:#222;display:flex;align-items:center;justify-content:center}

/* footer */
.footer{left:0;top:1065px;width:1003px;height:135px;background:linear-gradient(#b7a06a,#c9b583 60%,#bfa873)}
.footer h5{position:absolute;left:71px;top:12px;font-size:14px;font-weight:400;color:#2a2114;letter-spacing:.5px}
.map{position:absolute;left:71px;top:37px;width:87px;height:85px;border:1px solid #e8e0c8;background:linear-gradient(135deg,#eef0e6,#d9dccf)}
.fcontact{position:absolute;left:172px;top:43px;font-size:10.5px;line-height:14px;color:#fff}
.flinks{position:absolute;left:413px;top:35px;font-size:10.5px;color:#fff}
.copy{position:absolute;left:413px;top:69px;font-size:10.5px;color:#fff}
.social-foot{position:absolute;left:790px;top:32px;flex-wrap:wrap;width:200px;row-gap:6px}
.social-foot span{color:#fff}
</style>
</head>
<body>

<header class="abs header">
  <div class="abs brand">
    <div class="brand-mark"></div>
    <div class="brand-name">HOME CALVINA</div>
    <div class="brand-sub">REAL ESTATE</div>
  </div>
  <div class="abs login"><i></i>Login to Friendlane</div>
  <div class="abs social social-top">
    <span><b style="background:#4fb3e0"></b>Chirper</span>
    <span><b style="background:#f27022"></b>Pagelog</span>
    <span><b style="background:#1b6aa3"></b>Workline</span>
    <span><b style="background:#3a9a4a"></b>Searchly</span>
  </div>
  <div class="abs header-rule"></div>
</header>

<nav class="abs nav">
  <a class="home" href="#">Home</a>
  <div class="items">
    <a href="#">Company</a><span class="sep">|</span>
    <a href="#">Associates</a><span class="sep">|</span>
    <a href="#">Search Properties</a><span class="sep">|</span>
    <a href="#">Marketing and Design</a><span class="sep">|</span>
    <a href="#">Contact Us</a>
  </div>
</nav>
<div class="abs search-box">
  <svg width="14" height="14" viewBox="0 0 14 14"><circle cx="5.5" cy="5.5" r="4" fill="none" stroke="#555" stroke-width="1.5"/><line x1="8.5" y1="8.5" x2="13" y2="13" stroke="#555" stroke-width="2"/></svg>
  Search
</div>

<section class="abs hero">
  <div class="abs hero-frame">
    <div class="abs hero-photo" role="img" aria-label="White Mediterranean villa with terracotta roof, green shutters, shrubs and a swimming pool"></div>
  </div>
  <div class="abs hero-arrow left"><svg width="10" height="12" viewBox="0 0 10 12"><path d="M2 1l6 5-6 5" fill="none" stroke="#fff" stroke-width="2.5"/></svg></div>
  <div class="abs hero-arrow right"><svg width="10" height="12" viewBox="0 0 10 12"><path d="M8 1L2 6l6 5" fill="none" stroke="#fff" stroke-width="2.5"/></svg></div>
</section>

<section class="abs search-band">
  <div class="abs search-panel">
    <svg class="abs search-tag" viewBox="0 0 170 95"><path d="M5 0H130L170 47.5 130 95H5Q0 95 0 90V5Q0 0 5 0Z" fill="#1a1714"/></svg>
    <div class="abs search-tag"><span>SEARCH</span></div>
    <div class="abs field" style="left:188px;top:21px"><i class="radio on"></i>FOR SALE</div>
    <div class="abs field" style="left:188px;top:61px"><i class="radio"></i>FOR RENT</div>
    <div class="abs field" style="left:289px;top:20px">Property Type<div class="select"></div></div>
    <div class="abs field" style="left:308px;top:60px">City Name<div class="select"></div></div>
    <div class="abs field" style="left:512px;top:20px">Price Min<div class="select sm"></div></div>
    <div class="abs field" style="left:512px;top:60px">Price Max<div class="select sm"></div></div>
    <div class="abs field" style="left:696px;top:20px">Beds<div class="select sm"></div></div>
    <div class="abs field" style="left:696px;top:60px">Baths<div class="select sm"></div></div>
    <div class="abs btn-dark" style="left:837px;top:25px;width:104px;height:30px">SEARCH</div>
    <div class="abs adv" style="left:845px;top:68px">Advanced Search</div>
  </div>
</section>

<section class="abs register">
  <h3>Client Registration</h3>
  <div class="in" style="top:51px">User Name</div>
  <div class="in" style="top:92px">Password</div>
  <div class="abs btn-dark" style="left:108px;top:127px;width:96px;height:26px">SUBMIT</div>
</section>

<div class="abs card" style="left:255px">
  <div class="photo" role="img" aria-label="Brick family house with lawn and trees" style="background:linear-gradient(#a9c8e8,#9a7f6a 55%,#5f8a3c)"></div>
  <div class="cap">JOIN HOME CALVINA</div>
</div>
<div class="abs card" style="left:507px">
  <div class="photo" role="img" aria-label="Two-storey suburban house surrounded by trees" style="background:linear-gradient(#8fb2d6,#d6d0bc 50%,#4f7a38)"></div>
  <div class="cap">FEATURED DEVELOPMENTS</div>
</div>
<div class="abs card" style="left:748px">
  <div class="photo" role="img" aria-label="Twin modern skyscraper towers against blue sky" style="background:linear-gradient(#3a6fb8,#8fb4dc 60%,#c8d2da)"></div>
  <div class="cap">LIST YOUR PROPERTY</div>
</div>

<section class="abs lower">
  <h4 style="left:63px;top:35px">BLOG</h4>
  <div class="avatar" style="left:47px;top:69px" role="img" aria-label="Blog author portrait"><div></div></div>
  <div class="post" style="left:120px;top:75px"><span class="date">Apr 11, 2012</span>Nunc varius facilisis eros. Sed erat. In in velit quis arcu ornare laoreet. luctus massa.</div>
  <div class="avatar" style="left:47px;top:151px" role="img" aria-label="Blog author portrait"><div></div></div>
  <div class="post" style="left:120px;top:155px"><span class="date">Apr 11, 2012</span>Nunc varius facilisis eros. Sed erat. In in velit quis arcu ornare laoreet. luctus massa.</div>
  <div class="more" style="left:121px;top:223px">Read More</div>

  <h4 style="left:353px;top:35px">NEWS</h4>
  <div class="post" style="left:352px;top:71px;width:180px"><span class="date">Apr 11, 2012</span>Nunc varius facilisis eros. Sed erat. In in velit quis arcu ornare laoreet. luctus massa.</div>
  <div class="post" style="left:352px;top:153px;width:180px"><span class="date">Apr 11, 2012</span>Nunc varius facilisis eros. Sed erat. In in velit quis arcu ornare laoreet. luctus massa.</div>
  <div class="more" style="left:352px;top:228px">Read More</div>

  <h4 style="left:586px;top:35px">WHAT'S NEW</h4>
  <div class="dot" style="left:917px;top:34px"><svg width="6" height="8" viewBox="0 0 6 8"><path d="M5 1L1 4l4 3" fill="none" stroke="#fff" stroke-width="1.5"/></svg></div>
  <div class="dot" style="left:941px;top:34px"><svg width="6" height="8" viewBox="0 0 6 8"><path d="M1 1l4 3-4 3" fill="none" stroke="#fff" stroke-width="1.5"/></svg></div>

  <div class="listing" style="left:582px;top:67px">
    <div class="pic" role="img" aria-label="Modern multi-storey residential building" style="background:linear-gradient(#2e6bc2,#9fb6d3 55%,#6d6f72)"></div>
    <p>Nunc varius facilisis eros. Sed erat. In in velit quis arcu ornare l aoreet. luctus massa.</p>
  </div>
  <div class="price" style="left:583px;top:220px">$240</div>
  <div class="abs btn-dark" style="left:657px;top:212px;width:68px;height:24px">Details</div>

  <div class="listing" style="left:768px;top:67px">
    <div class="pic" role="img" aria-label="White villa with palm trees and a pool" style="background:linear-gradient(#8bb7e0,#e6e0cf 55%,#4fa8c8)"></div>
    <p>Nunc varius facilisis eros. Sed erat. In in velit quis arcu ornare l aoreet. luctus massa.</p>
  </div>
  <div class="price" style="left:770px;top:218px">$240</div>
  <div class="abs btn-dark" style="left:844px;top:210px;width:68px;height:24px">Details</div>
</section>

<footer class="abs footer">
  <h5>CONTACT</h5>
  <div class="map" role="img" aria-label="Street map of the office location"></div>
  <div class="fcontact">Nunc varius facilisis eros.<br>Sed erat. In in velit<br><span style="display:block;height:7px"></span>Phone : 555 014 2290<br>Email : info@homecalvina.com</div>
  <div class="flinks">Privacy Policy &nbsp;|&nbsp; Contact Us &nbsp;|&nbsp; Resources &nbsp;|&nbsp; Site Map</div>
  <div class="copy">© 2012 HomeCalvina Realestate, All Rights Reserved</div>
  <div class="social social-foot">
    <span><b style="background:#3a5a98"></b>Friendlane</span>
    <span><b style="background:#4fb3e0"></b>Chirper</span>
    <span><b style="background:#f27022"></b>Pagelog</span>
    <span><b style="background:#1b6aa3"></b>Workline</span>
    <span><b style="background:#3a9a4a"></b>Searchly</span>
  </div>
</footer>

</body>
</html>
```